BRIGHTDESK - Remote Tech Support Site

We are looking for a new very responsive and simple website for our brand Brightdesk.com - a remote technical support company.

This company supports customers Globally in different countries throughout Eur/ North America / South America / Asia etc (please keep this in mind and integrate into the idea).

Its important to us that the design is very explanatory, the customer should easily be able to figure out that we provide computer support right away ... I like one page responsive type designs as well without a bunch of menu items

Here are some similar sites we like - but still looking for a unique design that fits out brand "brightdesk" - I have upload also some layouts i like (but the designs are not important just the layouts), youll see it includes consumer business etc which is important.

VOLM.COM - I love how clean it is - nice and white easy to see everything

PLUMWIRE247.COM - also nice the layout and responsive one page design makes it easy to use

corvalfix.com - similar to plumwire design as well - you can get the idea im looking for between the two

You will notice those examples are much different then the attachments I added - again this is more of an idea for possible layouts .. attached is also the logo - could inspire color scheme / blue white black etc

Target Market(s)

Home consumers without computer knowledge , older age 45-65, small medium business ... computer repair - slow computers

Industry/Entity Type

Computer Repair

Logo Text

Brightdesk

Coding

Coded - Design and coding required

Number of Pages Required

1 page

Font styles to use
Sans Serif
Other font styles liked:
• your choice responsive

Colors

Designer to choose colors to be used in the design.

Requirements
Must have
• Clean - responsive - professional design - the name says it all - brightdesk
• CALL TO ACTIONS FOR "Get Help Now!" / "Learn More" etc
Nice to have
• We are looking for a new very responsive and simple website for our brand Brightdesk.com - a remote technical support company.
• This company supports customers Globally in different countries throughout Eur/ North America / South America / Asia etc (please keep this in mind and integrate into the idea).
• Its important to us that the design is very explanatory, the customer should easily be able to figure out that we provide computer support right away ... I like one page responsive type designs as well without a bunch of menu items
• Here are some similar sites we like - but still looking for a unique design that fits out brand "brightdesk" - I have upload also some layouts i like (but the designs are not important just the layouts), youll see it includes consumer business etc which is important.
• VOLM.COM - I love how clean it is - nice and white easy to see everything
• PLUMWIRE247.COM - also nice the layout and responsive one page design makes it easy to use
• corvalfix.com - similar to plumwire design as well - you can get the idea im looking for between the two
Should not have
• dark, packed page - bad small font -

```html
<!DOCTYPE html>
<html lang="en">
<head>
<meta charset="utf-8">
<title>Brightdesk – Remote Tech Support</title>
<link href="https://fonts.googleapis.com/css2?family=Open+Sans:wght@400;600;700;800&display=swap" rel="stylesheet">
<style>
:root{
  --blue:#1d8fe6;
  --blue-dark:#1470c2;
  --ink:#2c3036;
  --grey:#6f757c;
  --light:#f3f5f7;
  --line:#dde2e7;
  --dark:#4a4f56;
  --footer:#2a2c30;
  --white:#ffffff;
}
*{box-sizing:border-box;margin:0;padding:0}
html,body{width:1200px;height:4176px;overflow:hidden}
body{font-family:"Open Sans",Arial,sans-serif;color:var(--ink);background:var(--white);position:relative}
section,header,footer{position:absolute;left:0;width:1200px;overflow:hidden}
.abs{position:absolute}
.btn{display:inline-block;background:var(--blue);color:#fff;font-size:13px;font-weight:700;letter-spacing:.5px;padding:9px 20px;border-radius:3px;text-transform:uppercase}
.btn.ghost{background:transparent;border:2px solid #fff}
.title{font-size:30px;font-weight:700;text-align:center;width:100%}
.sub{font-size:14px;color:var(--grey);text-align:center;width:100%;margin-top:8px}
.photo{position:absolute}

/* header */
.site-header{top:0;height:112px;background:#fff;border-bottom:1px solid var(--line)}
.topbar{position:absolute;top:0;left:0;width:1200px;height:36px;font-size:12px;color:var(--grey)}
.lang{position:absolute;left:160px;top:9px;display:flex;align-items:center;gap:6px}
.lang i{display:block;width:20px;height:13px;background:var(--blue-dark)}
.contact-top{position:absolute;right:160px;top:9px;display:flex;gap:24px}
.navrow{position:absolute;top:36px;left:0;width:1200px;height:76px}
.logo{position:absolute;left:160px;top:18px;display:flex;align-items:center;gap:10px;font-size:30px;font-weight:700;color:var(--ink)}
.logo i{width:36px;height:36px;border-radius:50%;background:var(--blue);display:block}
.nav{position:absolute;left:490px;top:28px;display:flex;gap:32px;font-size:12px;font-weight:700;text-transform:uppercase;color:var(--ink)}
.nav .active{color:var(--blue)}
.navrow .btn{position:absolute;right:160px;top:20px}

/* hero */
.hero{top:112px;height:488px;background:linear-gradient(120deg,#dfe4e8 0%,#b9c3cc 45%,#8c98a5 100%)}
.hero-box{position:absolute;left:650px;top:272px;background:rgba(30,34,40,.75);color:#fff;padding:14px 22px}
.hero-box h1{font-size:36px;font-weight:800;line-height:1.1}
.hero-box p{font-size:28px;font-weight:600}
.hero .btn{position:absolute;left:660px;top:378px}

/* about */
.about{top:600px;height:340px;background:linear-gradient(90deg,#e6eef6 0%,#cfdcea 50%,#9fb3c7 100%)}
.about h2{position:absolute;left:160px;top:48px;font-size:30px;font-weight:700}
.about p{position:absolute;left:160px;top:110px;width:400px;font-size:13px;line-height:1.7;color:var(--grey)}
.about .btn{position:absolute;left:160px;top:232px}

/* realtime */
.realtime{top:940px;height:440px;background:linear-gradient(180deg,#fff,#f4f6f8)}
.realtime .title{position:absolute;top:44px}
.realtime .sub{position:absolute;top:90px}
.hub{position:absolute;left:505px;top:195px;width:190px;height:190px;border-radius:50%;border:6px solid var(--blue);background:#fff;display:flex;align-items:center;justify-content:center;gap:6px;font-size:24px;font-weight:700}
.hub i{width:16px;height:16px;border-radius:50%;background:var(--blue)}
.rt-item{position:absolute;display:flex;align-items:center;gap:14px;font-size:13px;font-weight:600;color:var(--blue-dark);width:300px}
.rt-item .ic{width:56px;height:56px;border-radius:50%;background:var(--ink);flex:none;display:flex;align-items:center;justify-content:center}
.rt-item.left{flex-direction:row-reverse;text-align:right}

/* how */
.how{top:1380px;height:420px;background:linear-gradient(135deg,#3f444b,#5b6068)}
.how .title,.how .sub{color:#fff;position:absolute}
.how .title{top:44px}.how .sub{top:90px;color:#d6d9dd}
.step{position:absolute;top:150px;width:260px;text-align:center;color:#fff}
.step .ic{width:76px;height:76px;margin:0 auto 18px;background:var(--blue);border-radius:6px;display:flex;align-items:center;justify-content:center}
.step h3{font-size:15px;font-weight:700;margin-bottom:8px}
.step p{font-size:12px;color:#d6d9dd;line-height:1.6}

/* features */
.features{top:1800px;height:512px;background:linear-gradient(180deg,#f7f8fa,#eceff2)}
.features .title{position:absolute;top:44px}.features .sub{position:absolute;top:90px}
.feat{position:absolute;width:210px;text-align:center}
.feat .ic{width:60px;height:60px;margin:0 auto 12px;display:flex;align-items:center;justify-content:center}
.feat h3{font-size:14px;font-weight:700;margin-bottom:6px}
.feat p{font-size:11px;color:var(--grey);line-height:1.5}

/* member band */
.member{top:2312px;height:108px;background:var(--blue);color:#fff}
.member h2{position:absolute;left:160px;top:36px;font-size:26px;font-weight:700}
.member .price{position:absolute;left:600px;top:24px;text-align:center;font-size:14px}
.member .price b{font-size:32px;font-weight:700}
.member .btn{position:absolute;right:160px;top:34px}

/* testimonials */
.testimonials{top:2420px;height:428px;background:#fff}
.testimonials .title{position:absolute;top:40px}
.client{position:absolute;top:110px;width:160px;text-align:center;font-size:11px;color:var(--grey)}
.client i{display:block;width:96px;height:96px;margin:0 auto 10px;border-radius:50%;background:linear-gradient(135deg,#c6ccd3,#7e8894);border:4px solid #fff;box-shadow:0 0 0 1px var(--line)}
.quote{position:absolute;left:170px;top:262px;width:860px;height:120px;background:var(--light);border:1px solid var(--line);padding:22px 50px;font-size:12px;line-height:1.7;color:var(--grey);text-align:center}
.quote b{position:absolute;left:18px;top:8px;font-size:40px;color:var(--line)}

/* pricing */
.pricing{top:2848px;height:584px;background:linear-gradient(180deg,#f5f7f9,#e7ebef)}
.pricing .title{position:absolute;top:44px}.pricing .sub{position:absolute;top:90px}
.plan{position:absolute;top:150px;width:220px;height:390px;background:#fff;border:1px solid var(--line);text-align:center}
.plan h3{font-size:18px;font-weight:700;padding:22px 0;border-bottom:1px solid var(--line)}
.plan .amt{font-size:30px;font-weight:700;color:var(--blue);margin-top:22px}
.plan .amt small{font-size:12px}
.plan .save{font-size:11px;color:var(--grey);margin-top:2px}
.plan ul{list-style:none;font-size:11px;color:var(--grey);margin-top:44px;line-height:2.2;border-top:1px solid var(--line);padding-top:10px}
.plan .btn{margin-top:40px;border-radius:16px;font-size:11px}
.plan.featured{top:132px;height:426px;width:250px;background:var(--blue);color:#fff;border:none}
.plan.featured h3{border-color:rgba(255,255,255,.3)}
.plan.featured .amt,.plan.featured .save,.plan.featured ul{color:#fff}
.plan.featured ul{border-color:rgba(255,255,255,.3)}
.plan.featured .btn{background:#fff;color:var(--blue)}

/* call */
.call{top:3432px;height:440px;background:linear-gradient(180deg,#1e8fe6,#1877cc);color:#fff}
.call .title{position:absolute;top:42px;font-size:34px}
.call .sub{position:absolute;top:92px;color:#d8ebfb}
.call h4{position:absolute;left:160px;top:180px;font-size:17px;font-weight:400}
.call .lead{position:absolute;left:160px;top:214px;width:440px;font-size:22px;line-height:1.35;font-weight:400}
.call .btn{position:absolute;left:160px;top:320px;background:transparent;border:2px solid #fff}
.laptop{position:absolute;left:700px;top:150px;width:300px;height:200px;border:10px solid #1d1f23;border-radius:8px 8px 0 0;background:linear-gradient(135deg,#c9b48a,#7a6a55)}
.laptop-base{position:absolute;left:672px;top:350px;width:356px;height:14px;background:#d0d4d9;border-radius:0 0 10px 10px}

/* footer */
.site-footer{top:3872px;height:304px;background:var(--footer);color:#b7bbc0;font-size:12px}
.fcol{position:absolute;top:36px}
.fcol h5{color:#fff;font-size:14px;font-weight:700;margin-bottom:16px}
.fcol li{list-style:none;line-height:2}
.nl-input{width:200px;height:28px;background:#fff;margin:10px 0 8px;border-radius:2px}
.badge{width:70px;height:34px;background:#e9e4d6;border-radius:4px;margin-bottom:8px}
.bottom{position:absolute;left:0;top:268px;width:1200px;height:36px;background:#1d1f22;font-size:11px}
.bottom span{position:absolute;left:160px;top:10px}
.social{position:absolute;right:160px;top:7px;display:flex;gap:8px}
.social i{width:22px;height:22px;border-radius:50%;background:var(--blue);display:block}
</style>
</head>
<body>

<header class="site-header">
  <div class="topbar">
    <div class="lang"><i></i>English ▾</div>
    <div class="contact-top"><span>☎ 800 · 555 · 0142</span><span>✉ info@brightdesk.com</span></div>
  </div>
  <div class="navrow">
    <div class="logo"><i></i>brightdesk</div>
    <nav class="nav"><span class="active">Home</span><span>About Us</span><span>Services</span><span>FAQs</span><span>Contact Us</span></nav>
    <span class="btn">Login</span>
  </div>
</header>

<section class="hero">
  <div class="photo" role="img" aria-label="Older couple smiling at a laptop at home" style="inset:0"></div>
  <div class="hero-box"><h1>DEDICATED SUPPORT</h1><p>Anytime. Anywhere.</p></div>
  <span class="btn">More Info</span>
</section>

<section class="about">
  <div class="photo" role="img" aria-label="Man working on a laptop at a desk" style="left:600px;top:0;width:600px;height:340px"></div>
  <h2>About Us</h2>
  <p>Our remote support team helps home users and small businesses fix slow computers, remove threats and set up new devices from anywhere in the world. We connect securely, explain every step and get you back to work fast.</p>
  <span class="btn">View Services</span>
</section>

<section class="realtime">
  <div class="title">Real-time Support Features And Benefits</div>
  <div class="sub">Lorem ipsum dolor sit amet, consectetuer adipiscing elit.</div>
  <div class="hub"><i></i>brightdesk</div>
  <div class="rt-item left" style="left:190px;top:160px"><span class="ic"><svg width="28" height="28" viewBox="0 0 28 28"><circle cx="14" cy="14" r="10" fill="none" stroke="#fff" stroke-width="3"/><path d="M14 8v6l4 3" stroke="#fff" stroke-width="3" fill="none"/></svg></span>Regular scan-ups and optimization</div>
  <div class="rt-item left" style="left:190px;top:330px"><span class="ic"><svg width="28" height="28" viewBox="0 0 28 28"><path d="M6 22 20 8M8 6l14 14" stroke="#fff" stroke-width="4"/></svg></span>Setup and Installation Included</div>
  <div class="rt-item" style="left:710px;top:160px"><span class="ic"><svg width="28" height="28" viewBox="0 0 28 28"><text x="14" y="19" fill="#fff" font-size="11" font-weight="700" text-anchor="middle" font-family="Open Sans,sans-serif">24/7</text></svg></span>24/7 Real-Time Technician Support</div>
  <div class="rt-item" style="left:710px;top:330px"><span class="ic"><svg width="28" height="28" viewBox="0 0 28 28"><path d="M14 3 24 7v7c0 6-4 10-10 12C8 24 4 20 4 14V7z" fill="#fff"/></svg></span>Premium Security Software in the Bundle</div>
</section>

<section class="how">
  <div class="photo" role="img" aria-label="Dimmed photo of people using computers" style="inset:0;background:rgba(0,0,0,.1)"></div>
  <div class="title">How It Works</div>
  <div class="sub">Lorem ipsum dolor sit amet, consectetuer adipiscing elit.</div>
  <div class="step" style="left:170px"><div class="ic"><svg width="40" height="40" viewBox="0 0 40 40"><circle cx="17" cy="17" r="10" fill="none" stroke="#fff" stroke-width="4"/><path d="M25 25l9 9" stroke="#fff" stroke-width="4"/></svg></div><h3>Free Diagnostic</h3><p>Our technician checks your PC<br>remotely and finds the issue.</p></div>
  <div class="step" style="left:470px"><div class="ic"><svg width="40" height="40" viewBox="0 0 40 40"><path d="M8 21l8 8 16-18" stroke="#fff" stroke-width="5" fill="none"/></svg></div><h3>Get Fixed</h3><p>We repair, tune and secure your<br>system while you watch.</p></div>
  <div class="step" style="left:770px"><div class="ic"><svg width="40" height="40" viewBox="0 0 40 40"><ellipse cx="20" cy="10" rx="12" ry="5" fill="#fff"/><path d="M8 14c0 3 5 5 12 5s12-2 12-5v6c0 3-5 5-12 5S8 23 8 20zM8 24c0 3 5 5 12 5s12-2 12-5v6c0 3-5 5-12 5S8 33 8 30z" fill="#fff"/></svg></div><h3>Backup your Information</h3><p>Your files are saved safely so<br>nothing is ever lost again.</p></div>
</section>

<section class="features">
  <div class="title">All The Best Features, At The Best Price!</div>
  <div class="sub">Lorem ipsum dolor sit amet, consectetuer adipiscing elit.</div>
  <div class="feat" style="left:155px;top:160px"><div class="ic"><svg width="44" height="44"><path d="M22 4 38 10v10c0 10-7 17-16 20C13 37 6 30 6 20V10z" fill="#1d8fe6"/></svg></div><h3>Ad Blocker</h3><p>Stop annoying pop-ups and ads<br>on every browser you use.</p></div>
  <div class="feat" style="left:380px;top:160px"><div class="ic"><svg width="44" height="44"><path d="M8 36 32 12M12 8l24 24" stroke="#1d8fe6" stroke-width="6"/></svg></div><h3>Regular Tune-Ups</h3><p>Keep your PC fast with regular<br>cleanups and optimization.</p></div>
  <div class="feat" style="left:610px;top:160px"><div class="ic"><svg width="44" height="44"><rect x="4" y="6" width="36" height="24" rx="2" fill="#1d8fe6"/><rect x="14" y="32" width="16" height="4" fill="#1d8fe6"/></svg></div><h3>System Reports</h3><p>Clear reports after every session<br>so you see what was done.</p></div>
  <div class="feat" style="left:835px;top:160px"><div class="ic"><svg width="44" height="44"><rect x="2" y="8" width="28" height="20" rx="2" fill="#1d8fe6"/><rect x="30" y="16" width="12" height="20" rx="2" fill="#1d8fe6"/></svg></div><h3>Multiple Devices</h3><p>Get support for up to five PCs,<br>laptops and tablets.</p></div>
  <div class="feat" style="left:155px;top:340px"><div class="ic"><svg width="44" height="44"><circle cx="22" cy="14" r="8" fill="#1d8fe6"/><path d="M8 40c0-9 6-14 14-14s14 5 14 14z" fill="#1d8fe6"/></svg></div><h3>Identity Protection</h3><p>Coming Soon.</p></div>
  <div class="feat" style="left:380px;top:340px"><div class="ic"><svg width="44" height="44"><rect x="12" y="2" width="20" height="40" rx="3" fill="#1d8fe6"/><rect x="15" y="7" width="14" height="26" fill="#fff"/></svg></div><h3>Mobile Security</h3><p>Coming Soon.</p></div>
  <div class="feat" style="left:610px;top:340px"><div class="ic"><svg width="44" height="44"><rect x="2" y="6" width="30" height="22" rx="2" fill="#1d8fe6"/><rect x="26" y="18" width="16" height="22" rx="2" fill="#1470c2"/></svg></div><h3>Cross Platform Support</h3><p>One Support Plan for different<br>types of devices.</p></div>
  <div class="feat" style="left:835px;top:340px"><div class="ic"><svg width="44" height="44"><path d="M12 34a9 9 0 0 1 0-18 12 12 0 0 1 23 3 8 8 0 0 1 0 15z" fill="#1d8fe6"/></svg></div><h3>Cloud Backup</h3><p>Save your files online and<br>restore them any time.</p></div>
</section>

<section class="member">
  <h2>Become a Member Today!</h2>
  <div class="price">Starting At Only<br><b>$19.99</b> /month</div>
  <span class="btn ghost">Get Started</span>
</section>

<section class="testimonials">
  <div class="title">Client Testimonials</div>
  <div class="client" style="left:220px"><i role="img" aria-label="Client portrait"></i>Mr. Alan Foster</div>
  <div class="client" style="left:430px"><i role="img" aria-label="Client portrait"></i>Mrs. Nora Bell</div>
  <div class="client" style="left:640px"><i role="img" aria-label="Client portrait"></i>Mr. Owen Hale</div>
  <div class="client" style="left:850px"><i role="img" aria-label="Client portrait"></i>Mrs. Ruth Vance</div>
  <div class="quote"><b>“</b>My computer was so slow I almost gave up on it. The technician connected in minutes, explained everything in plain words and made it faster than the day I bought it. Friendly, patient and honest service that I can recommend to anyone who is not good with computers. I now call them for every problem at home and at the office.</div>
</section>

<section class="pricing">
  <div class="title">Membership Pricing And Plans</div>
  <div class="sub">Lorem ipsum dolor sit amet, consectetuer adipiscing elit.</div>
  <div class="plan" style="left:170px"><h3>Premium</h3><div class="amt">$19.99 <small>/ Monthly</small></div><div class="save">($249 $300 saving/fee)</div><ul><li>Regular 90-Day Optimization</li><li>Unlimited 24/7 Live Technician Support</li></ul><span class="btn">Learn More</span></div>
  <div class="plan featured" style="left:475px"><h3>Premium Plus</h3><div class="amt">$29.99 <small>/ Monthly</small></div><div class="save">($349 $400 saving/fee)</div><ul><li>Regular 90-Day Optimization</li><li>Unlimited 24/7 Live Technician Support</li></ul><span class="btn">Learn More</span></div>
  <div class="plan" style="left:815px"><h3>Platinum</h3><div class="amt">$39.99 <small>/ Monthly</small></div><div class="save">($449 $500 saving/fee)</div><ul><li>Regular 90-Day Optimization</li><li>Unlimited 24/7 Live Technician Support</li></ul><span class="btn">Learn More</span></div>
</section>

<section class="call">
  <div class="title">CALL US TODAY</div>
  <div class="sub">Lorem ipsum dolor sit amet, consectetuer adipiscing elit.</div>
  <h4>And get started with our dedicated technicians</h4>
  <div class="lead">Get A <b>20 minute</b> One-on-one Free Consultation With One Of Our Experts!</div>
  <span class="btn">Get Started Now</span>
  <div class="laptop" role="img" aria-label="Laptop showing a support technician on a video call"></div>
  <div class="laptop-base"></div>
</section>

<footer class="site-footer">
  <div class="fcol" style="left:160px"><h5>Quick Links</h5><ul><li>› Home</li><li>› About Us</li><li>› Services</li><li>› FAQs</li><li>› Contact Us</li></ul></div>
  <div class="fcol" style="left:350px"><h5>Contact Details</h5><ul><li>⚲ BRIGHTDESK</li><li>&nbsp;&nbsp;&nbsp;410 Harbor Lane, Suite 12</li><li>&nbsp;&nbsp;&nbsp;Lakeview, CA 90210</li><li>☎ 800 · 555 · 0142</li><li>✉ info@brightdesk.com</li></ul></div>
  <div class="fcol" style="left:660px"><h5>Newsletter</h5><p>Subscribe for tips and offers.</p><div class="nl-input"></div><span class="btn" style="padding:6px 16px;font-size:11px">Subscribe</span></div>
  <div class="fcol" style="left:930px"><h5>Trusted By</h5><div class="badge"></div><div class="badge"></div><div class="badge"></div><div class="badge"></div></div>
  <div class="bottom"><span>Copyright © 2016. All rights reserved.</span><div class="social"><i></i><i></i><i></i></div></div>
</footer>

</body>
</html>
```